Bright Path Attorneys Billboard Design for Personal Injury Law Firm

Need a billboard design that we can use for different versions. 1400px X 400px jpeg or png
I have attached the logo and the attorney for the billboard. Attorney Marla Benning
Here is a link to our current website brightpathlegalgroup.example

HEADLINE: HIT BY A TRUCK?
SUBHEAD: NO FEE. BIG FIGHT.
877-GRANTLY

HEADLINE: ACCIDENT?
SUBHEAD: NO FEE, UNLESS WE WIN!
877-GRANTLY

HEADLINE: BIG TRUCK. BIG CASE.
SUBHEAD: YOU PAY $0 UPFRONT
877-GRANTLY

Target Market(s)

People in Car Accident

Industry/Entity Type

Personal Injury Attorneys

```html
<!DOCTYPE html>
<html lang="en">
<head>
<meta charset="utf-8">
<title>Bright Path Attorneys – Billboard Set</title>
<link href="https://fonts.googleapis.com/css2?family=Anton&display=swap" rel="stylesheet">
<style>
  :root {
    --backdrop-top: #fbfbfb;
    --backdrop-bottom: #b9b9b9;
    --board-dark: #0d0f0d;
    --board-green: #2f8f2f;
    --accent-green: #17d41d;
    --wedge-green: #3fd62c;
    --silver-top: #ffffff;
    --silver-mid: #c9c9c9;
    --ink-white: #ffffff;
  }
  * { box-sizing: border-box; margin: 0; padding: 0; }
  html, body { width: 979px; height: 1200px; overflow: hidden; }
  body {
    background: linear-gradient(180deg, var(--backdrop-top) 0%, var(--backdrop-bottom) 100%);
    font-family: "Anton", "Impact", sans-serif;
    position: relative;
  }
  .billboard {
    position: absolute;
    left: 33px;
    width: 887px;
    height: 336px;
    overflow: hidden;
    background:
      radial-gradient(ellipse 70% 80% at 60% 0%, rgba(70,170,60,.85) 0%, rgba(40,110,40,.55) 40%, rgba(13,15,13,0) 75%),
      linear-gradient(100deg, var(--board-dark) 0%, #142014 35%, var(--board-green) 100%);
    box-shadow: 4px 6px 10px rgba(0,0,0,.45);
  }
  .billboard--truck { top: 23px; }
  .billboard--accident { top: 395px; }
  .billboard--case { top: 775px; }

  .billboard__photo {
    position: absolute;
    top: 0; right: 0; bottom: 0;
    -webkit-mask-image: linear-gradient(90deg, transparent 0%, #000 30%);
    mask-image: linear-gradient(90deg, transparent 0%, #000 30%);
  }
  .billboard--truck .billboard__photo {
    left: 470px;
    background: linear-gradient(160deg, #dfe3e3 0%, #9ea4a6 45%, #5b6064 75%, #3a8a32 100%);
  }
  .billboard--accident .billboard__photo {
    left: 560px;
    background: linear-gradient(150deg, #8f9a9c 0%, #4d5558 45%, #23292b 80%, #1c2a1c 100%);
  }
  .billboard--case .billboard__photo {
    left: 590px;
    background: linear-gradient(150deg, #b3262b 0%, #7e1a1d 40%, #2a2d30 75%, #161a18 100%);
  }

  .billboard__wedge {
    position: absolute;
    inset: 0;
    width: 887px;
    height: 336px;
  }

  .billboard__line {
    position: absolute;
    left: 48px;
    white-space: nowrap;
    line-height: 1;
    text-transform: uppercase;
    letter-spacing: -0.5px;
  }
  .billboard__line--silver {
    background: linear-gradient(180deg, var(--silver-top) 0%, var(--silver-top) 45%, var(--silver-mid) 100%);
    -webkit-background-clip: text;
    background-clip: text;
    color: transparent;
    filter: drop-shadow(3px 4px 3px rgba(0,0,0,.6));
  }
  .billboard__phone {
    color: var(--accent-green);
    font-size: 80px;
    top: 212px;
    filter: drop-shadow(3px 4px 3px rgba(0,0,0,.55));
  }

  .billboard--truck .billboard__headline { font-size: 94px; top: 20px; }
  .billboard--truck .billboard__subhead { font-size: 87px; top: 117px; }

  .billboard--accident .billboard__headline { font-size: 112px; top: 8px; }
  .billboard--accident .billboard__subhead { font-size: 72px; top: 126px; }

  .billboard--case .billboard__headline { font-size: 87px; top: 35px; }
  .billboard--case .billboard__subhead { font-size: 84px; top: 118px; }

  .brand {
    position: absolute;
    right: 26px;
    bottom: 22px;
    display: flex;
    align-items: center;
    gap: 8px;
    color: var(--ink-white);
    font-size: 19px;
    letter-spacing: 1px;
    line-height: 1;
  }
  .brand__dot {
    width: 14px; height: 14px;
    border-radius: 50%;
    background: var(--accent-green);
  }
</style>
</head>
<body>

  <section class="billboard billboard--truck">
    <div class="billboard__photo" role="img" aria-label="Photo of a white semi truck colliding with a wrecked silver sedan"></div>
    <svg class="billboard__wedge" viewBox="0 0 887 336" aria-hidden="true">
      <polygon points="328,336 887,190 887,336" fill="var(--wedge-green)"/>
    </svg>
    <p class="billboard__line billboard__line--silver billboard__headline">Hit by a truck?</p>
    <p class="billboard__line billboard__line--silver billboard__subhead">No fee. Big fight</p>
    <p class="billboard__line billboard__phone">877-GRANTLY</p>
    <div class="brand"><span class="brand__dot"></span><span class="brand__name">BRIGHT PATH ATTORNEYS</span></div>
  </section>

  <section class="billboard billboard--accident">
    <div class="billboard__photo" role="img" aria-label="Close-up photo of a damaged grey SUV front end on a road"></div>
    <svg class="billboard__wedge" viewBox="0 0 887 336" aria-hidden="true">
      <polygon points="328,336 887,190 887,336" fill="var(--wedge-green)" opacity=".9"/>
    </svg>
    <p class="billboard__line billboard__line--silver billboard__headline">Accident?</p>
    <p class="billboard__line billboard__line--silver billboard__subhead">No fee, unless we win!</p>
    <p class="billboard__line billboard__phone">877-GRANTLY</p>
    <div class="brand"><span class="brand__dot"></span><span class="brand__name">BRIGHT PATH ATTORNEYS</span></div>
  </section>

  <section class="billboard billboard--case">
    <div class="billboard__photo" role="img" aria-label="Close-up photo of a crashed red truck front with shattered headlight"></div>
    <svg class="billboard__wedge" viewBox="0 0 887 336" aria-hidden="true">
      <polygon points="328,336 887,190 887,336" fill="var(--wedge-green)" opacity=".9"/>
    </svg>
    <p class="billboard__line billboard__line--silver billboard__headline">Big truck. Big case.</p>
    <p class="billboard__line billboard__line--silver billboard__subhead">You pay $0 upfront</p>
    <p class="billboard__line billboard__phone">877-GRANTLY</p>
    <div class="brand"><span class="brand__dot"></span><span class="brand__name">BRIGHT PATH ATTORNEYS</span></div>
  </section>

</body>
</html>
```